Ductless Mini Split Business Website

Amber Kite Services is looking to design an eye catching educational website about installing Ductless mini splits.

Similar to this company.
https://www.cedarcoolair.com/

```html
<!DOCTYPE html>
<html lang="en">
<head>
<meta charset="utf-8">
<title>Amber Kite Services – Ductless Mini Splits</title>
<link href="https://fonts.googleapis.com/css2?family=Barlow+Semi+Condensed:wght@500;600;700&family=Lato:wght@400;700&display=swap" rel="stylesheet">
<style>
:root{
  --yellow:#f2c313;
  --yellow-dark:#e3ae0a;
  --navy:#16263f;
  --ink:#121212;
  --text:#333;
  --muted:#555;
  --grey:#e9e9e9;
  --light:#f4f4f4;
  --field:#f2f2f2;
  --white:#fff;
}
*{box-sizing:border-box;margin:0;padding:0}
html,body{width:1200px;height:5227px;overflow:hidden;background:var(--white)}
body{font-family:"Lato",sans-serif;color:var(--text)}
.page{position:relative;width:1200px;height:5227px;overflow:hidden}
.abs{position:absolute}
.head{font-family:"Barlow Semi Condensed",sans-serif;font-weight:700;color:var(--ink);line-height:1}
.kicker{font-family:"Barlow Semi Condensed",sans-serif;font-weight:500;font-size:24px;color:var(--ink)}
.center{text-align:center;left:0;width:1200px}
.photo{position:absolute}
.btn{position:absolute;background:linear-gradient(var(--yellow),var(--yellow-dark));color:var(--ink);font:700 16px "Lato",sans-serif;display:flex;align-items:center;justify-content:center;letter-spacing:.3px}

/* header */
.topbar{top:10px;left:500px;display:flex;gap:48px;font-size:13px;color:var(--yellow)}
.topbar span{display:flex;align-items:center;gap:6px}
.social-top{top:4px;left:955px;display:flex;gap:8px}
.dot{width:24px;height:24px;border-radius:50%;background:var(--yellow)}
.nav{top:40px;left:0;width:1200px;height:54px}
.nav ul{position:absolute;top:18px;left:508px;list-style:none;display:flex;font-size:14px;color:var(--ink)}
.nav li{padding:0 18px;border-left:1px solid var(--ink);line-height:14px}
.nav li:first-child{border:0}
.logo{top:0;left:158px;width:134px;height:134px;border-radius:50%;background:var(--white);display:flex;align-items:center;justify-content:center;text-align:center;font:700 15px/1.2 "Lato",sans-serif;color:var(--ink)}

/* hero */
.hero-title{top:205px;left:156px;color:var(--white);font-family:"Barlow Semi Condensed",sans-serif;line-height:.95}
.hero-title .l1{font-size:60px;font-weight:500;display:block}
.hero-title .l2{font-size:92px;font-weight:700;display:block}
.hero-title .l3{font-size:84px;font-weight:500;display:block}

/* about */
.about-box{left:599px;top:859px;width:442px;height:355px;border:8px solid var(--yellow);background:var(--white);padding:38px 34px 0 30px;text-align:right}
.about-box .k{font-family:"Barlow Semi Condensed",sans-serif;font-size:24px;font-weight:500;color:var(--ink);text-align:left;padding-left:68px}
.about-box .t{font-size:66px;text-align:left;padding-left:68px}
.about-box .e{font-family:"Barlow Semi Condensed",sans-serif;font-size:24px;font-weight:600;color:var(--ink);margin-top:10px}
.about-box p{font-size:13px;line-height:21px;color:var(--muted);margin-top:6px}

/* services */
.card{position:absolute;top:1488px;width:281px;height:428px}
.card .back{position:absolute;left:0;top:0;width:281px;height:173px;background:#5a5a5a}
.card .img{left:22px;top:22px;width:241px;height:191px}
.card .body{position:absolute;left:22px;top:213px;width:241px;height:172px;background:var(--white);text-align:center;padding:18px 14px 0}
.card h3{font:600 20px "Barlow Semi Condensed",sans-serif;color:var(--ink)}
.card p{font-size:13px;line-height:19px;color:var(--muted);margin-top:8px}
.card .btn{left:47px;top:386px;width:187px;height:42px}
.arrow{width:26px;height:26px;border-radius:50%;background:#555;top:1703px;display:flex;align-items:center;justify-content:center}

/* benefits */
.perk{position:absolute;left:0;width:612px;height:86px;background:linear-gradient(90deg,rgba(22,38,63,0) 0%,#8b93a0 30%,var(--navy) 80%)}
.perk .txt{position:absolute;right:105px;top:12px;text-align:right;color:var(--white)}
.perk h4{font:700 22px "Barlow Semi Condensed",sans-serif;color:var(--white)}
.perk p{font-size:14px;line-height:18px}
.perk .ic{position:absolute;right:0;top:-2px;width:90px;height:90px;border-radius:50%;background:var(--yellow);border:3px solid var(--white);display:flex;align-items:center;justify-content:center}

/* testimonial */
.quote-box{left:481px;top:2923px;width:560px;height:351px;border:8px solid var(--yellow);background:var(--white);text-align:center;padding:96px 60px 0}
.quote-box p{font-size:13.5px;line-height:21px;color:var(--muted)}
.quote-box .who{margin-top:22px}

/* blog */
.post{position:absolute;top:3548px;width:286px}
.post .img{position:relative;width:286px;height:174px}
.post h3{font:600 21px "Barlow Semi Condensed",sans-serif;color:var(--ink);margin-top:14px}
.post .date{font-size:11px;color:var(--muted);margin-top:8px}
.post p{font-size:13px;line-height:18px;color:var(--muted);margin-top:5px}
.post .more{font-size:13px;font-weight:700;color:var(--ink);margin-top:3px}

/* contact */
.field{position:absolute;background:var(--field);border:1px solid #e1e1e1;font-size:12px;color:var(--muted);padding:18px 14px}

/* footer */
.ft-h{font:600 20px "Barlow Semi Condensed",sans-serif;color:var(--yellow);position:absolute;top:4888px}
.ft-list{position:absolute;top:4940px;left:158px;list-style:none;font-size:13px;color:var(--white);line-height:27.7px}
.ft-contact{position:absolute;left:412px;font-size:13px;color:var(--white);display:flex;gap:12px;line-height:20px}
.ring{width:30px;height:30px;border-radius:50%;border:2px solid var(--white);position:absolute;top:5103px}
</style>
</head>
<body>
<div class="page">

<!-- HERO -->
<svg class="abs" style="top:0;left:0" width="1200" height="660" viewBox="0 0 1200 660">
  <defs>
    <linearGradient id="heroSky" x1="0" y1="0" x2="1" y2="1">
      <stop offset="0" stop-color="#3b5d9a"/><stop offset=".6" stop-color="#5a7fc2"/><stop offset="1" stop-color="#6c90cf"/>
    </linearGradient>
  </defs>
  <polygon points="0,0 1200,0 1200,540 600,650 0,528" fill="url(#heroSky)"/>
  <polygon points="0,0 385,0 0,203" fill="#1d2e52"/>
  <polygon points="0,528 600,650 380,650 0,560" fill="#6e9a3a"/>
  <polygon points="600,650 1200,538 1200,546 612,654" fill="var(--yellow)"/>
</svg>
<div class="abs" role="img" aria-label="Outdoor ductless mini split condenser unit mounted on a blue wall above green shrubs" style="left:660px;top:250px;width:380px;height:300px"></div>

<div class="abs nav">
  <svg class="abs" width="1200" height="54"><polygon points="330,0 1200,0 1200,54 300,54" fill="var(--yellow)"/></svg>
  <ul><li>Home</li><li>About Us</li><li>Services</li><li>testmonial</li><li>Blog</li><li>Contact Us</li></ul>
</div>
<div class="abs topbar">
  <span><svg width="12" height="12" viewBox="0 0 24 24"><path fill="var(--yellow)" d="M6.6 10.8a15 15 0 006.6 6.6l2.2-2.2c.3-.3.7-.4 1-.2 1.1.4 2.3.6 3.6.6.6 0 1 .4 1 1V20c0 .6-.4 1-1 1A17 17 0 013 4c0-.6.4-1 1-1h3.5c.6 0 1 .4 1 1 0 1.2.2 2.4.6 3.6.1.3 0 .7-.2 1z"/></svg>555-204-318</span>
  <span><svg width="13" height="10" viewBox="0 0 26 20"><rect x="1" y="1" width="24" height="18" fill="none" stroke="var(--yellow)" stroke-width="2"/><path d="M1 1l12 10L25 1" fill="none" stroke="var(--yellow)" stroke-width="2"/></svg>amberkite@mail.com</span>
</div>
<div class="abs social-top"><div class="dot"></div><div class="dot"></div><div class="dot"></div></div>
<div class="abs logo">Amber Kite<br>Services</div>

<h1 class="abs hero-title"><span class="l1">INSTALLING</span><span class="l2">DUCTLESS</span><span class="l3">Mini Splits</span></h1>
<div class="btn" style="left:156px;top:430px;width:331px;height:45px">GET IN TOUCH WITH US</div>

<!-- ABOUT -->
<div class="photo" role="img" aria-label="Technician in a hard hat servicing an outdoor mini split unit" style="left:276px;top:731px;width:322px;height:483px;background:linear-gradient(135deg,#c9ccd0,#8a8f96 55%,#2d3340)"></div>
<div class="photo" role="img" aria-label="Cartoon bee mascot holding a wrench" style="left:152px;top:1035px;width:173px;height:193px;background:radial-gradient(circle at 50% 55%,#f1c21a 0,#e0b21a 38%,rgba(255,255,255,0) 70%)"></div>
<div class="abs about-box">
  <div class="k">About</div>
  <div class="head t">DUCTLESS</div>
  <div class="e">EXPERTS</div>
  <p>It is a long established fact that a reader will be distracted by the readable content of a page when looking at its layout. The point of using Lorem Ipsum is that it has a more-or-less normal distribution of letters,</p>
</div>

<!-- SERVICES -->
<svg class="abs" style="top:1300px;left:0" width="1200" height="1420" viewBox="0 0 1200 1420">
  <rect x="0" y="0" width="1200" height="1420" fill="var(--light)"/>
  <polygon points="0,598 600,0 1200,598 1200,1110 600,1400 0,1110" fill="var(--grey)"/>
  <polygon points="0,0 1200,0 1200,598 600,700 0,598" fill="var(--ink)"/>
</svg>
<div class="abs kicker center" style="top:1370px;text-align:center;color:var(--white)">How Can</div>
<div class="abs head center" style="top:1400px;font-size:66px;text-align:center;color:var(--white)">WE HELP YOU</div>

<div class="card" style="left:158px"><div class="back"></div><div class="photo img" role="img" aria-label="Technician mounting an indoor mini split head on a wall" style="background:linear-gradient(#f0f0f0,#9aa3ad)"></div><div class="body"><h3>Long Established Fact</h3><p>It is a long established fact that a reader will be distracted by the readable content</p></div><div class="btn">READ MORE</div></div>
<div class="card" style="left:457px"><div class="back"></div><div class="photo img" role="img" aria-label="Two outdoor condenser units against a grey wall" style="background:linear-gradient(#d8dbe0,#aeb3ba)"></div><div class="body"><h3>Long Established Fact</h3><p>It is a long established fact that a reader will be distracted by the readable content</p></div><div class="btn">READ MORE</div></div>
<div class="card" style="left:757px"><div class="back"></div><div class="photo img" role="img" aria-label="Technician cleaning the filter of an indoor unit" style="background:linear-gradient(#ededed,#5d6878)"></div><div class="body"><h3>Long Established Fact</h3><p>It is a long established fact that a reader will be distracted by the readable content</p></div><div class="btn">READ MORE</div></div>
<div class="abs arrow" style="left:130px"><svg width="10" height="10"><path d="M7 1L3 5l4 4" stroke="#fff" fill="none" stroke-width="1.5"/></svg></div>
<div class="abs arrow" style="left:1043px"><svg width="10" height="10"><path d="M3 1l4 4-4 4" stroke="#fff" fill="none" stroke-width="1.5"/></svg></div>

<!-- BENEFITS -->
<div class="abs kicker" style="left:158px;top:2120px">How Can</div>
<div class="abs head" style="left:158px;top:2146px;font-size:66px">WE HELP YOU</div>
<div class="perk" style="top:2229px"><div class="txt"><h4>0% FINANCING</h4><p>Lorem Ipsum has been the industry's<br>standard dummy text ever when an unknown</p></div><div class="ic"><svg width="40" height="40" viewBox="0 0 40 40" fill="none" stroke="var(--ink)" stroke-width="2"><rect x="8" y="6" width="24" height="28" rx="2"/><path d="M14 14h12M14 20h12M14 26h8"/></svg></div></div>
<div class="perk" style="top:2330px"><div class="txt"><h4>365 DAY, MONEY BACK GUARANTEE</h4><p>Lorem Ipsum has been the industry's<br>standard dummy text ever when an unknown</p></div><div class="ic"><svg width="40" height="40" viewBox="0 0 40 40" fill="none" stroke="var(--ink)" stroke-width="2"><circle cx="22" cy="13" r="8"/><path d="M4 30l8-6h10l8 4-8 6H12"/></svg></div></div>
<div class="perk" style="top:2434px"><div class="txt"><h4>EXPERTS IN DUCTLESS</h4><p>Lorem Ipsum has been the industry's<br>standard dummy text ever when an unknown</p></div><div class="ic"><svg width="40" height="40" viewBox="0 0 40 40" fill="none" stroke="var(--ink)" stroke-width="2"><path d="M20 5l12 5v9c0 8-6 13-12 15C14 32 8 27 8 19v-9z"/><path d="M14 20l4 4 8-8"/></svg></div></div>
<div class="photo" role="img" aria-label="Illustrated repairman in blue overalls carrying an air conditioner unit beside a red toolbox" style="left:710px;top:2050px;width:407px;height:538px;background:radial-gradient(ellipse at 50% 45%,#6f93d8 0,#3d62b5 35%,rgba(233,233,233,0) 70%)"></div>

<!-- TESTIMONIAL -->
<div class="photo" role="img" aria-label="Smiling client in a blue shirt" style="left:158px;top:2795px;width:322px;height:479px;background:linear-gradient(160deg,#d6d7d9,#9fb3c8 70%,#6f8aa8)"></div>
<div class="abs kicker" style="left:514px;top:2818px">Testimonial</div>
<div class="abs head" style="left:514px;top:2846px;font-size:66px">WHAT CLIENT SAY</div>
<div class="abs quote-box">
  <p>"It is a long established fact that a reader will be distracted by the readable content of a page when looking at its layout. The point of using Lorem Ipsum is that it has a more-or-less normal distribution of letters,"</p>
  <p class="who">- JoHN Doe<br>system analytics</p>
  <svg style="margin-top:24px" width="60" height="16" viewBox="0 0 60 16" fill="none" stroke-width="1.5"><path d="M18 8H4m5-5L4 8l5 5" stroke="#aaa"/><path d="M38 8h16m-5-5 5 5-5 5" stroke="var(--ink)"/></svg>
</div>

<!-- BLOG -->
<div class="abs kicker center" style="top:3430px;text-align:center">Blog</div>
<div class="abs head center" style="top:3458px;font-size:66px;text-align:center">LATEST BLOG</div>
<div class="post" style="left:158px"><div class="photo img" role="img" aria-label="Technician wiping an indoor mini split with a blue cloth" style="background:linear-gradient(#f4f4f4,#2e4f8f)"></div><h3>Long Established Fact</h3><div class="date">Date : 26-12-2019</div><p>It is a long established fact that a reader will be distracted by the read content</p><div class="more">READ MORE</div></div>
<div class="post" style="left:457px"><div class="photo img" role="img" aria-label="Hands removing the front panel of an indoor unit" style="background:linear-gradient(#e8e8e8,#4a4a4a)"></div><h3>Long Established Fact</h3><div class="date">Date : 26-12-2019</div><p>It is a long established fact that a reader will be distracted by the read content</p><div class="more">READ MORE</div></div>
<div class="post" style="left:757px"><div class="photo img" role="img" aria-label="Hand adjusting a wall thermostat" style="background:linear-gradient(#cfd6dc,#b07a5c)"></div><h3>Long Established Fact</h3><div class="date">Date : 26-12-2019</div><p>It is a long established fact that a reader will be distracted by the read content</p><div class="more">READ MORE</div></div>

<!-- CALL BAND -->
<svg class="abs" style="top:3958px;left:0" width="1200" height="360" viewBox="0 0 1200 360">
  <rect x="0" y="0" width="1200" height="173" fill="var(--navy)"/>
  <polygon points="0,173 340,173 0,345" fill="var(--navy)"/>
  <circle cx="300" cy="86" r="142" fill="var(--white)"/>
</svg>
<div class="photo" role="img" aria-label="Cartoon bee mascot with a wrench" style="left:190px;top:3952px;width:230px;height:190px;background:radial-gradient(circle at 50% 55%,#f1c21a 0,#e0b21a 40%,rgba(255,255,255,0) 72%)"></div>
<div class="abs" style="left:544px;top:4018px;display:flex;align-items:center;gap:6px;font:700 30px 'Barlow Semi Condensed',sans-serif;color:var(--white)">
  <svg width="22" height="22" viewBox="0 0 24 24"><path fill="#fff" d="M6.6 10.8a15 15 0 006.6 6.6l2.2-2.2c.3-.3.7-.4 1-.2 1.1.4 2.3.6 3.6.6.6 0 1 .4 1 1V20c0 .6-.4 1-1 1A17 17 0 013 4c0-.6.4-1 1-1h3.5c.6 0 1 .4 1 1 0 1.2.2 2.4.6 3.6.1.3 0 .7-.2 1z"/></svg>
  Call Us Now : <span style="color:var(--yellow);font-size:50px;margin-left:6px">555-204-318</span>
</div>

<!-- CONTACT -->
<div class="abs kicker center" style="top:4212px;text-align:center">Get In Touch</div>
<div class="abs head center" style="top:4240px;font-size:66px;text-align:center">CONTACT US TODAY</div>
<div class="field" style="left:195px;top:4320px;width:400px;height:53px">First Name :</div>
<div class="field" style="left:603px;top:4320px;width:400px;height:53px">Last Name :</div>
<div class="field" style="left:195px;top:4383px;width:400px;height:53px">Email :</div>
<div class="field" style="left:603px;top:4383px;width:400px;height:53px">Phone No :</div>
<div class="field" style="left:195px;top:4446px;width:808px;height:101px;padding-top:14px">Message :</div>
<div class="btn" style="left:438px;top:4559px;width:329px;height:45px">SUBMIT NOW</div>

<!-- FOOTER -->
<svg class="abs" style="top:4680px;left:0" width="1200" height="547" viewBox="0 0 1200 547">
  <polygon points="0,120 600,0 1200,60 1200,547 0,547" fill="var(--ink)"/>
  <polygon points="0,114 600,-4 600,6 0,126" fill="var(--yellow)"/>
</svg>
<div class="ft-h" style="left:158px">Quick Link</div>
<ul class="ft-list"><li>Home</li><li>About Us</li><li>Services</li><li>Testimonial</li><li>Blog</li><li>Contact Us</li></ul>
<div class="ft-h" style="left:412px">Contact Us</div>
<div class="ft-contact" style="top:4940px"><svg width="12" height="12" viewBox="0 0 24 24" style="margin-top:4px"><path fill="#fff" d="M6.6 10.8a15 15 0 006.6 6.6l2.2-2.2c.3-.3.7-.4 1-.2 1.1.4 2.3.6 3.6.6.6 0 1 .4 1 1V20c0 .6-.4 1-1 1A17 17 0 013 4c0-.6.4-1 1-1h3.5c.6 0 1 .4 1 1 0 1.2.2 2.4.6 3.6.1.3 0 .7-.2 1z"/></svg>555-204-318</div>
<div class="ft-contact" style="top:4993px"><svg width="12" height="14" viewBox="0 0 24 28" style="margin-top:3px"><path fill="#fff" d="M12 0a10 10 0 00-10 10c0 8 10 18 10 18s10-10 10-18A10 10 0 0012 0zm0 14a4 4 0 110-8 4 4 0 010 8z"/></svg>2750 Harbor Lane,<br>Lorem Ipsum</div>
<div class="ft-contact" style="top:5062px"><svg width="13" height="10" viewBox="0 0 26 20" style="margin-top:5px"><rect x="1" y="1" width="24" height="18" fill="none" stroke="#fff" stroke-width="2"/><path d="M1 1l12 10L25 1" fill="none" stroke="#fff" stroke-width="2"/></svg>hello@amberkiteservices.com</div>
<div class="ft-h" style="left:682px">Subscribe Newletter</div>
<div class="abs" style="left:682px;top:4933px;width:331px;height:47px;background:var(--white);font-size:14px;color:var(--text);padding:15px 20px">Enter Your Mail Id</div>
<div class="btn" style="left:682px;top:4994px;width:331px;height:43px;font-size:15px">SIGN UP NOW</div>
<div class="ring" style="left:683px"></div><div class="ring" style="left:720px"></div><div class="ring" style="left:757px"></div><div class="ring" style="left:794px"></div>
<div class="abs" style="left:154px;top:5123px;font-size:11px;color:var(--white)">Copyright©2019 Amberkiteservices. All Rights Reserved</div>

</div>
</body>
</html>
```